Business Cards

I'd like help creating business cards with the full logo "Veltrona Capital Partners" on the back of the card (navy background with white writing), and abbreviated logo "VCP" on the front. Would like to list name, title, phone number, email, and website listed on front of card. Would like to keep very simple. Front font Arial or similar.

```html
<!DOCTYPE html>
<html lang="en">
<head>
<meta charset="utf-8">
<title>Veltrona Capital Partners – Business Cards</title>
<link href="https://fonts.googleapis.com/css2?family=Arimo:wght@400;700&display=swap" rel="stylesheet">
<style>
  :root {
    --navy: #1f3a70;
    --silver: #b9bcc1;
    --swoosh: #b5b7ba;
    --ink: #1a1a1a;
    --paper: #ffffff;
    --backdrop: #2b2c31;
  }
  * { margin: 0; padding: 0; box-sizing: border-box; }
  html, body { width: 1200px; height: 864px; overflow: hidden; }
  body {
    background: var(--backdrop);
    font-family: "Arimo", Arial, sans-serif;
    display: flex;
    flex-direction: column;
    align-items: center;
    justify-content: center;
    gap: 40px;
  }
  .card {
    width: 560px;
    height: 320px;
    position: relative;
    overflow: hidden;
  }

  /* Back of card */
  .card-back {
    background: var(--navy);
    display: flex;
    align-items: center;
    justify-content: center;
  }
  .brand-full {
    display: flex;
    align-items: center;
    gap: 18px;
  }
  .brand-square {
    width: 22px;
    height: 22px;
    background: var(--silver);
  }
  .brand-full-name {
    color: var(--silver);
    font-weight: 700;
    font-size: 27px;
    letter-spacing: 3px;
    text-transform: uppercase;
  }

  /* Front of card */
  .card-front { background: var(--paper); }
  .card-front .wave {
    position: absolute;
    inset: 0;
    width: 100%;
    height: 100%;
  }
  .brand-short {
    position: absolute;
    left: 42px;
    top: 128px;
    color: var(--navy);
    font-weight: 700;
    font-size: 64px;
    letter-spacing: 1px;
  }
  .divider {
    position: absolute;
    left: 262px;
    top: 44px;
    width: 1px;
    height: 92px;
    background: var(--navy);
  }
  .contact {
    position: absolute;
    left: 282px;
    top: 38px;
  }
  .contact-name {
    color: var(--navy);
    font-weight: 700;
    font-size: 21px;
    letter-spacing: 0.3px;
  }
  .contact-title {
    color: var(--ink);
    font-size: 14px;
    margin: 3px 0 9px;
  }
  .contact-list { list-style: none; }
  .contact-list li {
    display: flex;
    align-items: center;
    gap: 8px;
    color: var(--ink);
    font-size: 14px;
    line-height: 21px;
  }
  .contact-list svg { width: 12px; height: 12px; fill: var(--navy); flex: none; }
</style>
</head>
<body>

  <section class="card card-back" aria-label="Card back">
    <div class="brand-full">
      <span class="brand-square"></span>
      <span class="brand-full-name">Veltrona Capital Partners</span>
    </div>
  </section>

  <section class="card card-front" aria-label="Card front">
    <svg class="wave" viewBox="0 0 560 320" preserveAspectRatio="none" aria-hidden="true">
      <path d="M0 300 C 200 312, 330 282, 410 222 C 460 185, 505 172, 560 168 L560 320 L0 320 Z" fill="var(--navy)"/>
      <path d="M150 292 C 290 290, 340 262, 405 208 C 455 168, 500 158, 548 154 C 500 166, 460 178, 412 214 C 350 262, 290 294, 150 292 Z" fill="var(--swoosh)"/>
    </svg>

    <div class="brand-short">VCP</div>
    <div class="divider"></div>

    <div class="contact">
      <h1 class="contact-name">DARA WHITCOMBE</h1>
      <p class="contact-title">General Manager</p>
      <ul class="contact-list">
        <li>
          <svg viewBox="0 0 24 24"><path d="M6.6 10.8a15.1 15.1 0 0 0 6.6 6.6l2.2-2.2c.3-.3.7-.4 1-.2 1.1.4 2.3.6 3.6.6.6 0 1 .4 1 1V20c0 .6-.4 1-1 1A17 17 0 0 1 3 4c0-.6.4-1 1-1h3.5c.6 0 1 .4 1 1 0 1.3.2 2.5.6 3.6.1.3 0 .7-.2 1z"/></svg>
          555-014-2297
        </li>
        <li>
          <svg viewBox="0 0 24 24"><path d="M2 5h20v14H2z"/><path d="M3 6l9 7 9-7" fill="none" stroke="#fff" stroke-width="1.6"/></svg>
          hello@veltronacap.com
        </li>
        <li>
          <svg viewBox="0 0 24 24"><circle cx="12" cy="12" r="10"/><path d="M2 12h20M12 2c3 3 3 17 0 20M12 2c-3 3-3 17 0 20" fill="none" stroke="#fff" stroke-width="1.4"/></svg>
          www.veltronacap.com
        </li>
      </ul>
    </div>
  </section>

</body>
</html>
```